Information flyer for 5 day treatment flyer

I am wanting a double sided flyer for my next 5 day treatment program for addictions. I have included the copy for the flyer as an attachment.
I have also included a file vault link to my brand guidelines and my logos. The logo I prefer is the grey horse with the words Lumen Circle under.
https://files.example-share.net/sh/k2m9x7q1zt/AAB3pLr8Wc?dl=0

https://files.example-share.net/s/h7w2n5v8rb/LUMEN%20CIRCLE%20%7C%20Brand%20Identity%20Guidelines.pdf?dl=0
I have also included a copy of an existing flyer which I like very much and a documant with the copy.
https://files.example-share.net/sh/q8d3j6t2yk/AACmN4fZ9Hs?dl=0

I prefer simple, elegant designs please. The design needs to show my clients that I know what I am doing and I am trust worthy and a skilled professional.

Here is the file vault link to the images I have selected for this program. The tones in the images I have selected are orange/red. Please feel free to pick what you think works well.
https://files.example-share.net/sh/r5b1c9g4wp/AADkT7eQ2Jv?dl=0

Many thanks
Margot

```html
<!DOCTYPE html>
<html lang="en">
<head>
<meta charset="utf-8">
<title>Lumen Circle – Behind Closed Doors Flyer</title>
<link href="https://fonts.googleapis.com/css2?family=Montserrat:wght@400;600;700;800&family=Open+Sans:wght@400;600;700&display=swap" rel="stylesheet">
<style>
  :root{
    --brown:#8a6544;
    --tan:#a4805a;
    --deep:#3a2a1c;
    --ink:#161310;
    --grey:#5a5550;
    --band:#4a4744;
    --paper:#ffffff;
    --stage:#e4e4e4;
    --sun-top:#ecdcae;
    --sun-mid:#d6ad62;
    --shade:#2b2118;
  }
  *{box-sizing:border-box;margin:0;padding:0}
  html,body{width:768px;height:1200px;overflow:hidden}
  body{background:var(--stage);font-family:"Open Sans",Arial,sans-serif;position:relative}
  .page{position:absolute;left:176px;width:416px;height:588px;overflow:hidden;box-shadow:0 6px 18px rgba(0,0,0,.18)}
  .page--front{top:6px}
  .page--back{top:604px;background:var(--paper)}
  .abs{position:absolute}

  /* FRONT */
  .hero-photo{position:absolute;inset:0;background:
      radial-gradient(ellipse 120px 90px at 200px 270px,#fff7d8 0%,rgba(255,240,190,.6) 45%,rgba(255,240,190,0) 100%),
      linear-gradient(180deg,var(--sun-top) 0%,#e2c587 30%,var(--sun-mid) 52%,#8a6a3e 64%,#4a3826 72%,var(--shade) 82%,#1e1710 100%)}
  .frame{position:absolute;inset:0}
  .brand{left:26px;top:30px;width:110px;text-align:center}
  .brand__dot{width:26px;height:26px;border-radius:50%;background:var(--grey);margin:0 auto 8px}
  .brand__name{font-family:"Montserrat",sans-serif;font-weight:400;font-size:9px;letter-spacing:2px;color:var(--deep)}
  .big-num{left:142px;top:4px;font-family:"Montserrat",sans-serif;font-weight:600;font-size:86px;line-height:1;color:transparent;-webkit-text-stroke:2px var(--deep);letter-spacing:-6px}
  .days{left:240px;top:46px;font-family:"Montserrat",sans-serif;font-weight:700;font-size:22px;line-height:22px;color:var(--deep)}
  .days span{display:block;font-size:24px}
  .program{left:146px;top:94px;font-family:"Montserrat",sans-serif;font-weight:800;font-size:17.5px;color:var(--deep);letter-spacing:.2px}
  .title-band{left:30px;top:120px;width:356px;height:34px;background:var(--ink);color:#fff;font-family:"Montserrat",sans-serif;font-weight:600;font-size:25px;line-height:34px;text-align:center;letter-spacing:.5px}
  .subtitle{left:38px;top:160px;width:340px;font-size:12px;line-height:16px;color:var(--deep)}
  .qa-label{font-family:"Montserrat",sans-serif;font-size:6.5px;font-weight:600;letter-spacing:.8px;color:var(--tan)}
  .qa-text{width:252px;font-size:5.4px;line-height:7px;color:#f2e9dc}
  .foot-bar{left:0;top:558px;width:416px;height:20px;background:var(--ink);color:#fff;text-align:center;font-family:"Montserrat",sans-serif;font-weight:700;font-size:7.5px;letter-spacing:2px;line-height:20px}

  /* BACK */
  .h-sect{font-family:"Montserrat",sans-serif;font-weight:700;font-size:6.4px;color:var(--brown);letter-spacing:.3px;text-transform:uppercase;line-height:8px}
  .copy{font-size:5.3px;line-height:6.8px;color:var(--grey)}
  .intro{left:18px;top:18px;width:380px}
  .intro p{margin-top:3px;margin-bottom:5px}
  .outcomes{left:0;top:162px;width:225px;height:278px;background:var(--brown);padding:12px 16px 0 18px}
  .outcomes .h-sect{color:#fff}
  .outcomes ul{list-style:none;margin-top:8px}
  .outcomes li{position:relative;padding-left:6px;font-size:5.2px;line-height:6.4px;color:#fff;margin-bottom:6.3px}
  .outcomes li::before{content:"";position:absolute;left:0;top:2.4px;width:2px;height:2px;background:#fff;border-radius:50%}
  .when{left:246px;top:174px;width:160px}
  .when__tag{display:inline-block;margin-top:8px;background:var(--brown);color:#fff;font-family:"Montserrat",sans-serif;font-weight:700;font-size:6px;padding:2px 6px}
  .schedule{margin-top:3px;border-collapse:separate;border-spacing:3px 3px;margin-left:-3px}
  .schedule td{border:.6px solid #aaa;font-size:5px;color:var(--grey);padding:1.5px 3px;white-space:nowrap}
  .door-photo{left:225px;top:286px;width:191px;height:154px;background:
      radial-gradient(ellipse 40px 55px at 95px 75px,#f6d49a 0%,#d9875a 40%,rgba(120,110,110,0) 100%),
      linear-gradient(180deg,#c9c7c4 0%,#a8a5a0 50%,#8d8780 100%)}
  .enrol{left:0;top:440px;width:416px;height:30px;background:var(--band);color:#fff;display:flex;align-items:center;padding:0 14px 0 12px;gap:12px}
  .enrol__label{font-family:"Montserrat",sans-serif;font-weight:700;font-size:5.8px;line-height:7px;width:52px}
  .enrol__text{font-size:5.2px;line-height:6.4px}
  .inclusions{left:18px;top:480px;width:180px}
  .inclusions ul{list-style:none;margin-top:4px}
  .inclusions li{font-size:5.2px;line-height:7.2px;color:var(--grey)}
  .inclusions li::before{content:"• "}
  .invest{left:218px;top:480px;width:182px}
  .invest p{margin-top:4px;text-align:justify}
  .company{left:134px;top:548px;width:180px;height:12px;background:var(--brown);color:#fff;font-size:5.6px;line-height:12px;text-align:center}
  .company-rule{left:18px;top:554px;width:382px;height:.6px;background:#bbb}
  .contact{left:18px;top:568px;width:390px;display:flex;gap:10px;font-size:5px;color:var(--grey);align-items:center}
  .contact span{display:flex;align-items:center;gap:2px}
  .contact svg{width:6px;height:6px;fill:var(--brown)}
</style>
</head>
<body>

<section class="page page--front">
  <div class="hero-photo" role="img" aria-label="Sunset beach photo: a woman sitting on a rock with head in hands while a man walks away, silhouetted against the sea"></div>
  <svg class="frame" width="416" height="588" viewBox="0 0 416 588">
    <polyline points="150,112 22,112 22,548" fill="none" stroke="var(--deep)" stroke-width="1.6"/>
    <polyline points="394,156 394,548" fill="none" stroke="var(--deep)" stroke-width="1.6"/>
  </svg>

  <div class="abs brand">
    <div class="brand__dot"></div>
    <div class="brand__name">LUMEN CIRCLE</div>
  </div>
  <div class="abs big-num">12</div>
  <div class="abs days">DAYS<span>INTENSIVE</span></div>
  <div class="abs program">TREATMENT PROGRAM</div>
  <div class="abs title-band">BEHIND CLOSED DOORS</div>
  <p class="abs subtitle">Break destructive relationship patterns and learn how to create more love and intimacy</p>

  <div class="abs qa-label" style="left:32px;top:456px">WHAT IS INTIMACY?</div>
  <p class="abs qa-text" style="left:130px;top:440px">Intimacy is our emotional food - it sustains and nourishes us, helping us feel connected, understood and valued. Lack of emotional intimacy in our most important relationships creates problems such as anxiety, jealousy, withdrawal, betrayal, abandonment and even infidelity.</p>
  <div class="abs qa-label" style="left:30px;top:506px">HUNGER VERSUS LOVE.</div>
  <p class="abs qa-text" style="left:130px;top:482px">Emotional hunger is not love. This hunger is a strong need caused by emotional deprivation in childhood. Feelings of emotional hunger are experienced as deep internal sensations that range in intensity from a dull ache to a sharp painful feeling. Because of its intensity, this sensation is often confused with real love. Many people claim to be loving and caring, when in fact they are actually feeling their emotional hunger and neediness. Emotional hunger is what we experience when feeling abandonment pain. This keeps us in unfulfilling, destructive and addictive relationships.</p>
  <div class="abs foot-bar">www.lumencircle.example</div>
</section>

<section class="page page--back">
  <div class="abs intro">
    <h2 class="h-sect">This program focuses on abandonment and engulfment issues.</h2>
    <p class="copy">To avoid the pain of abandonment and the overwhelming feelings of engulfment, in childhood we subconsciously learn to create a fantasy bond. Later this bond is transferred to our adult relationships, especially romantic and sexual ones. The fantasy bond is a primary defense against intimacy.</p>
    <p class="copy">According to Dr. Elaine Hart, "the fantasy bond is a substitute for love and care that was missing in the child's world. Many parents offer affection and love when they feel the need for it themselves. This type of physical affection drains the emotional resources of children rather than nourishing them. It is a form of taking, not giving.</p>
    <h2 class="h-sect" style="margin-top:8px">Why is it important to examine our childhood when trying to sort out our<br>issues in adult relationships today?</h2>
    <p class="copy">Children are needy by nature, not by choice. They instinctively adapt their behaviour and personalities in order to get their emotional needs met. As a result of the fantasy bond, created between child and caregiver, we carry with us into adulthood the same survival mechanisms leading to a sacrifice of our freedom and any real intimacy in loving relationships. Instead we create dependencies with people, substances and behaviour patterns to fill the deep emptiness or loneliness within us.</p>
  </div>

  <div class="abs outcomes">
    <h3 class="h-sect">During this 12 day intensive<br>program you will</h3>
    <ul>
      <li>Identify what you need to do for yourself to stop destructive relationship patterns.</li>
      <li>Learn how to protect yourself from feeling overwhelmed or drained in close relationships.</li>
      <li>Release emotional baggage from past adult relationships.</li>
      <li>Significantly heal childhood abandonment and engulfment issues.</li>
      <li>Identify the subconscious negative beliefs that are sabotaging you from having the relationship you desire.</li>
      <li>Release childhood trauma out of your body from abuse and neglect.</li>
      <li>Learn how to set healthy boundaries - physically, emotionally, spiritually, intellectually and sexually.</li>
      <li>Differentiate between needs and values - the drivers in relationships.</li>
      <li>Identify your needs and values and determine steps to take to meet them.</li>
      <li>Free yourself of shame, guilt and fear from childhood and adult relationships.</li>
      <li>Communicate your needs and ask for what you want without feeling too embarrassed or vulnerable.</li>
      <li>Create healthy self-esteem and love - the foundation for intimacy.</li>
    </ul>
  </div>

  <div class="abs when">
    <h3 class="h-sect">During this 12 day intensive<br>program you will</h3>
    <span class="when__tag">WHEN</span>
    <table class="schedule">
      <tr><td>Thursday</td><td>25th October</td><td>6:00pm - 9:00pm</td></tr>
      <tr><td>Friday</td><td>26th October</td><td>9:00pm - 5:00pm</td></tr>
      <tr><td>Saturday</td><td>27th October</td><td>9:00pm - 9:00pm</td></tr>
      <tr><td>Sunday</td><td>28th October</td><td>9:00pm - 5:00pm</td></tr>
      <tr><td>Monday</td><td>29th October</td><td>9:00pm - 4:00pm</td></tr>
    </table>
  </div>
  <div class="abs door-photo" role="img" aria-label="Photo of open double doors revealing a glowing orange sunset sky"></div>

  <div class="abs enrol">
    <div class="enrol__label">ENROLMENT PROCESS</div>
    <p class="enrol__text">This 5 day program is limited in numbers and offers individual and group time. Enrolments close Friday, 19th October 2018. To book your place, register your interest or find out more about this program please call Margot 0400 000 123. Out of town participants please contact our office for assistance with accommodation if required.</p>
  </div>

  <div class="abs inclusions">
    <h3 class="h-sect">Inclusions</h3>
    <ul>
      <li>A pre-assessment phone consult</li>
      <li>Relevant on online diagnostic surveys</li>
      <li>Integrated Equine Assisted Psychotherapy</li>
      <li>Ropes course</li>
      <li>All course materials (notebook, writing materials).</li>
      <li>Morning and afternoon tea daily.</li>
    </ul>
  </div>
  <div class="abs invest">
    <h3 class="h-sect">Investments: ($2250 including GST)</h3>
    <p class="copy">TERMS &amp; CONDITIONS: A non-refundable deposit of $500 is required to hold your place. Enrolments with full payment is required by Tuesday, 23th October 2018. Charge card transactions incur a 3.3% merchant fee, credit card and debit card 2.5%. EFTPOS facility available.</p>
  </div>

  <div class="abs company-rule"></div>
  <div class="abs company">Lumen Circle Pty Ltd. ABN 00 000 000 000</div>

  <div class="abs contact">
    <span><svg viewBox="0 0 10 10"><path d="M2 1l2 2-1 1.5c.7 1.4 1.6 2.3 3 3L7.5 6l2 2-1.3 1.5C4.5 9 1 5.5.5 1.8z"/></svg>0400 000 123</span>
    <span><svg viewBox="0 0 10 10"><path d="M0 2h10v6H0zM0 2l5 3.5L10 2" stroke="#fff" stroke-width=".6"/></svg>margot@lumencircle.example</span>
    <span><svg viewBox="0 0 10 10"><circle cx="5" cy="5" r="4.5"/></svg>www.lumencircle.example</span>
    <span><svg viewBox="0 0 10 10"><path d="M5 0a3.5 3.5 0 0 1 3.5 3.5C8.5 6 5 10 5 10S1.5 6 1.5 3.5A3.5 3.5 0 0 1 5 0z"/></svg>42 Harbour Lane, Fernvale NSW 2000</span>
  </div>
</section>

</body>
</html>
```